arts & crafts

I collect old plates & make them into serving plates for cakes, afternoon teas, special occasions, weddings, parties, bridal showers. cake competitions, displays in bakeries.

Contact Information for Business Card

Tulips Turn Gold
Old plates set for new tables
Ph 0412873905
info@ tulipsturngold.com.au
www.tulipsturngold.com.au
friendpage
Craftly

```html
<!DOCTYPE html>
<html lang="en">
<head>
<meta charset="utf-8">
<title>Tulips Turn Gold – Business Card</title>
<link rel="stylesheet" href="https://fonts.googleapis.com/css2?family=Montserrat:wght@400;500&family=Questrial&display=swap">
<style>
  :root {
    --backdrop: #e4e4e4;
    --card: #f5f5f3;
    --ink: #1a1a1a;
    --rule: #8a8a8a;
    --ring-blue: #1c9fdc;
    --accent-black: #111111;
    --brand-plum: #5b1f52;
    --tagline-grey: #3c3c3c;
  }
  * { margin: 0; padding: 0; box-sizing: border-box; }
  html, body {
    width: 1200px;
    height: 900px;
    overflow: hidden;
    background: var(--backdrop);
  }
  .business-card {
    position: absolute;
    left: 160px;
    top: 200px;
    width: 880px;
    height: 500px;
    background: var(--card);
    overflow: hidden;
    box-shadow: 0 2px 6px rgba(0,0,0,0.12);
  }
  .contact-block {
    position: absolute;
    left: 90px;
    top: 110px;
    width: 260px;
    text-align: center;
    font-family: "Montserrat", sans-serif;
    color: var(--ink);
  }
  .holder-name {
    font-size: 38px;
    font-weight: 500;
    letter-spacing: 2px;
    line-height: 1;
  }
  .holder-role {
    margin-top: 8px;
    font-size: 11px;
    letter-spacing: 1.5px;
  }
  .divider {
    margin: 14px auto 12px;
    width: 250px;
    border: 0;
    border-top: 1px solid var(--rule);
  }
  .contact-lines {
    list-style: none;
    font-size: 16px;
    line-height: 1.45;
  }
  .emblem-art {
    position: absolute;
    left: 0;
    top: 0;
  }
  .brand-lockup {
    position: absolute;
    left: 435px;
    top: 212px;
    width: 360px;
    text-align: center;
  }
  .brand-name {
    display: flex;
    align-items: center;
    justify-content: center;
    gap: 12px;
    font-family: "Montserrat", sans-serif;
    font-weight: 500;
    font-size: 34px;
    color: var(--brand-plum);
    line-height: 1;
  }
  .brand-dot {
    width: 24px;
    height: 24px;
    border-radius: 50%;
    background: var(--ring-blue);
    flex: none;
  }
  .tagline {
    margin-top: 12px;
    font-family: "Questrial", sans-serif;
    font-size: 21px;
    letter-spacing: 1.5px;
    color: var(--tagline-grey);
  }
</style>
</head>
<body>
  <main class="business-card">
    <svg class="emblem-art" width="880" height="500" viewBox="0 0 880 500" aria-hidden="true">
      <circle cx="598" cy="262" r="210" fill="var(--accent-black)"/>
      <circle cx="615" cy="250" r="200" fill="var(--card)" stroke="var(--ring-blue)" stroke-width="7"/>
    </svg>

    <section class="contact-block">
      <h1 class="holder-name">JANE DOE</h1>
      <p class="holder-role">OWNER</p>
      <hr class="divider">
      <ul class="contact-lines">
        <li>Ph 0412873905</li>
        <li>info@ tulipsturngold.com.au</li>
        <li>www.tulipsturngold.com.au</li>
        <li>friendpage</li>
        <li>Craftly</li>
      </ul>
    </section>

    <section class="brand-lockup">
      <p class="brand-name"><span>Tulips Turn Gold</span><span class="brand-dot"></span></p>
      <p class="tagline">Old plates set for new tables</p>
    </section>
  </main>
</body>
</html>
```